Vantor Scorecard

Redesign KLT's existing Vantor scorecard, which tracks and reports key performance indicators (KPIs) for our clients. The scorecard provides our customers with an at-a-glance view of our on-site performance. Vantor is a tool that automatically populates and reports this data.

Review the attached document and deliver suggested redesign options for the two attached views.
Page 1: Portfolio-wide views (high level rollup of multiple sites)
Page 2: Site-level view
Updates

Project Deadline Extended
Reason: Due to the holiday season within the U.S. around the globe we have decided to extend out deadline in hopes of gaining more participation. We will also be providing comments to the current designs tomorrow.

Font styles to use
Sans Serif

Requirements
Must have
• - Sans serif fonts
- Clean aesthetic
- Utilize the exact key performance indicators as are in the attached mockup
- White background (think Plum-esque)
Nice to have
• - Ideas for animation of design elements
Should not have
• - Pictures (icons are okay)

```html
<!DOCTYPE html>
<html lang="en">
<head>
<meta charset="utf-8">
<title>Scorecard Dashboard</title>
<link href="https://fonts.googleapis.com/css2?family=Roboto:wght@100;300;400;700&display=swap" rel="stylesheet">
<style>
:root{
  --frame:#555555;
  --panel:#e6e6e6;
  --page:#ffffff;
  --ink:#3d3d3d;
  --muted:#8a8a8a;
  --button:#ffffff;
  --rule:#c8c8c8;
  --alert:#e0262b;
  --bar:#444444;
}
*{box-sizing:border-box;margin:0;padding:0}
html,body{width:1200px;height:1000px;overflow:hidden;background:var(--page);font-family:'Roboto',Arial,sans-serif;color:var(--ink)}
.board{position:relative;width:1200px;height:1000px}
.detail-column{position:absolute;left:0;top:0;width:597px;height:1000px;background:var(--frame)}
.panel{position:absolute;background:var(--panel);overflow:hidden}
.abs{position:absolute;white-space:nowrap}
.brand-dot{position:absolute;border-radius:50%;background:var(--ink)}
.brand-name{position:absolute;font-weight:700;color:var(--ink);line-height:1;white-space:nowrap}
.brand-rule{position:absolute;width:1px;background:var(--ink)}
.scope{position:absolute;font-weight:300;color:var(--ink);line-height:1.1;white-space:nowrap}
.product{position:absolute;font-weight:700;color:var(--ink);line-height:1;white-space:nowrap}
.nav-btn{position:absolute;background:var(--button);border:1px solid #d6d6d6;box-shadow:0 1px 3px rgba(0,0,0,.18);display:flex;align-items:center;color:var(--muted);font-weight:300;white-space:nowrap}
.nav-btn svg{flex:none;fill:none;stroke:#555;stroke-width:1.6}
.title{position:absolute;font-weight:100;color:var(--ink);line-height:1;white-space:nowrap}
.subtitle{position:absolute;font-weight:700;color:#555;line-height:1;white-space:nowrap}
.period{position:absolute;font-weight:300;color:#777;line-height:1;white-space:nowrap}
.score-label{position:absolute;font-weight:700;color:var(--ink);line-height:.95;white-space:nowrap}
.score-label .goal-value{font-weight:400}
.gauge{position:absolute}
.gauge-value{position:absolute;font-weight:400;color:var(--ink);text-align:center;line-height:1}
.kpi-table{position:absolute;border-collapse:collapse;color:var(--ink)}
.kpi-table th{background:#fff;font-weight:700;text-align:left;vertical-align:middle}
.kpi-table td,.kpi-table th{border:1px solid var(--rule);white-space:nowrap}
.kpi-table .num{text-align:center}
.kpi-table .miss{color:var(--alert)}
.small-table{left:650px;top:760px;width:507px;font-size:8.6px}
.small-table th{height:33px;padding:0 3px;line-height:1.05}
.small-table td{height:16.6px;padding:0 3px;font-weight:300}
.small-table .total td{font-weight:400}
.small-table .total .num{font-weight:700}
.big-table{left:32px;top:45px;font-size:24px;table-layout:fixed;width:700px}
.big-table th{height:86px;font-size:26px;padding:0 8px;line-height:1;box-shadow:0 2px 4px rgba(0,0,0,.15)}
.big-table td{height:45px;padding:0 8px;font-weight:300}
</style>
</head>
<body>
<svg width="0" height="0" style="position:absolute" aria-hidden="true">
  <defs>
    <symbol id="ico-org" viewBox="0 0 24 24"><rect x="9" y="3" width="6" height="5"/><rect x="2" y="16" width="6" height="5"/><rect x="9" y="16" width="6" height="5"/><rect x="16" y="16" width="6" height="5"/><path d="M12 8v4M5 16v-4h14v4M12 12v4"/></symbol>
    <symbol id="ico-bars" viewBox="0 0 24 24"><path d="M5 20v-6M10 20V8M15 20v-9M20 20V4" stroke-width="3.4"/></symbol>
    <symbol id="ico-person" viewBox="0 0 24 24"><rect x="3" y="9" width="18" height="11" fill="#555"/><circle cx="12" cy="7" r="4" fill="#555"/></symbol>
    <symbol id="ico-board" viewBox="0 0 24 24"><rect x="7" y="4" width="15" height="11"/><circle cx="4" cy="8" r="2" fill="#555"/><path d="M4 11v9M4 13l6-3"/></symbol>
    <symbol id="ico-cloud" viewBox="0 0 24 24"><path d="M7 19h11a4 4 0 0 0 0-8 6 6 0 0 0-11.5-1A4.5 4.5 0 0 0 7 19z"/><path d="M12 17v-6M9.5 13.5 12 11l2.5 2.5"/></symbol>
    <symbol id="ico-check" viewBox="0 0 24 24"><circle cx="12" cy="12" r="10" fill="#555" stroke="none"/><path d="M7.5 12.5l3 3 6-6.5" stroke="#fff" stroke-width="2.4"/></symbol>
    <symbol id="ico-helmet" viewBox="0 0 24 24"><path d="M5 13a7 7 0 0 1 14 0z" fill="#555"/><path d="M4 14h16"/><path d="M7 16c0 4 10 4 10 0" fill="#555"/><path d="M12 6v4"/></symbol>
    <symbol id="gauge-ring" viewBox="0 0 100 100">
      <circle cx="50" cy="50" r="45" fill="#e4e4e4" stroke="#4a4a4a" stroke-width="7"/>
      <path d="M50 50 L50 9 A41 41 0 0 1 83 26 Z" fill="#bdbdbd"/>
      <circle cx="50" cy="50" r="28" fill="#e4e4e4"/>
    </symbol>
  </defs>
</svg>

<div class="board">
  <div class="detail-column">
    <section class="panel" style="left:8px;top:8px;width:582px;height:482px">
      <span class="brand-dot" style="left:44px;top:36px;width:72px;height:72px"></span>
      <span class="brand-name" style="left:139px;top:48px;font-size:44px">company</span>
      <span class="brand-rule" style="left:332px;top:32px;height:64px"></span>
      <span class="scope" style="left:345px;top:40px;font-size:20px">All sites<br>All Programs | July 2013</span>

      <div class="nav-btn" style="left:40px;top:132px;width:235px;height:73px;font-size:30px;padding-left:14px;gap:12px"><svg width="38" height="38"><use href="#ico-org"/></svg>Governance</div>
      <div class="nav-btn" style="left:298px;top:132px;width:146px;height:73px;font-size:30px;padding-left:18px;gap:12px"><svg width="30" height="30"><use href="#ico-bars"/></svg>Cost</div>
      <div class="nav-btn" style="left:467px;top:132px;width:220px;height:73px;font-size:30px;padding-left:14px;gap:12px"><svg width="38" height="38"><use href="#ico-org"/></svg>Innovations</div>
      <div class="nav-btn" style="left:40px;top:222px;width:193px;height:74px;font-size:30px;padding-left:10px;gap:18px"><svg width="36" height="36"><use href="#ico-cloud"/></svg>Updates</div>
      <div class="nav-btn" style="left:256px;top:222px;width:181px;height:74px;font-size:30px;padding-left:18px;gap:16px"><svg width="36" height="36"><use href="#ico-check"/></svg>Quality</div>
      <div class="nav-btn" style="left:460px;top:222px;width:160px;height:74px;font-size:30px;padding-left:16px;gap:14px"><svg width="40" height="40"><use href="#ico-helmet"/></svg>EHS</div>

      <span class="title" style="left:42px;top:336px;font-size:74px">Scorecard</span>
      <span class="subtitle" style="left:44px;top:408px;font-size:24px">KPI Score by Site</span>
      <span class="period" style="left:43px;top:434px;font-size:25px">Showing July 2013</span>
    </section>

    <section class="panel" style="left:8px;top:500px;width:582px;height:233px">
      <span class="score-label" style="left:225px;top:30px;font-size:40px">Site Score<br>Goal <span class="goal-value">90%</span></span>
      <svg class="gauge" style="left:440px;top:8px" width="124" height="124"><use href="#gauge-ring"/></svg>
      <span class="gauge-value" style="left:440px;top:50px;width:124px;font-size:38px">86%</span>
      <svg class="abs" style="left:0;top:170px" width="582" height="63" role="img" aria-label="Detail of site score bars">
        <line x1="0" y1="18" x2="582" y2="18" stroke="#9a9a9a" stroke-dasharray="3 3"/>
        <g fill="var(--bar)">
          <rect x="0" y="18" width="18" height="45"/><rect x="25" y="48" width="25" height="15"/><rect x="55" y="60" width="25" height="3"/>
          <rect x="85" y="18" width="25" height="45"/><rect x="115" y="48" width="25" height="15"/><rect x="145" y="60" width="25" height="3"/>
          <rect x="175" y="18" width="25" height="45"/><rect x="205" y="60" width="25" height="3"/><rect x="235" y="60" width="25" height="3"/>
          <rect x="265" y="18" width="25" height="45"/><rect x="295" y="48" width="25" height="15"/><rect x="325" y="60" width="25" height="3"/>
          <rect x="355" y="60" width="25" height="3"/><rect x="385" y="18" width="25" height="45"/><rect x="415" y="48" width="25" height="15"/>
          <rect x="445" y="60" width="25" height="3"/><rect x="475" y="18" width="25" height="45"/><rect x="505" y="48" width="25" height="15"/>
          <rect x="535" y="60" width="25" height="3"/><rect x="565" y="60" width="25" height="3"/>
        </g>
      </svg>
    </section>

    <section class="panel" style="left:8px;top:742px;width:582px;height:251px">
      <table class="kpi-table big-table">
        <colgroup><col style="width:373px"><col style="width:125px"><col style="width:202px"></colgroup>
        <tr><th>Key Performance Indicator</th><th class="num">KPI<br>Score</th><th>Target</th></tr>
        <tr><td>Complaints</td><td class="num miss">4.0</td><td>Less than</td></tr>
        <tr><td>Quality Audits</td><td class="num">3.2</td><td>3 out of</td></tr>
        <tr><td>Customer Surveys</td><td class="num">4.7</td><td>4 out of</td></tr>
      </table>
    </section>
  </div>

  <section class="panel" style="left:628px;top:0;width:544px;height:482px">
    <span class="brand-dot" style="left:22px;top:22px;width:30px;height:30px"></span>
    <span class="brand-name" style="left:64px;top:29px;font-size:18px">company</span>
    <span class="brand-rule" style="left:145px;top:24px;height:24px"></span>
    <span class="scope" style="left:153px;top:27px;font-size:8.5px">All sites<br>All Programs | July 2013</span>
    <span class="product" style="right:20px;top:24px;font-size:23px">KLTVantor</span>

    <div class="nav-btn" style="left:22px;top:66px;width:100px;height:32px;font-size:13px;padding-left:6px;gap:5px"><svg width="17" height="17"><use href="#ico-org"/></svg>Governance</div>
    <div class="nav-btn" style="left:133px;top:66px;width:61px;height:32px;font-size:13px;padding-left:8px;gap:5px"><svg width="13" height="13"><use href="#ico-bars"/></svg>Cost</div>
    <div class="nav-btn" style="left:207px;top:66px;width:100px;height:32px;font-size:13px;padding-left:6px;gap:5px"><svg width="17" height="17"><use href="#ico-org"/></svg>Innovations</div>
    <div class="nav-btn" style="left:318px;top:66px;width:94px;height:32px;font-size:13px;padding-left:8px;gap:7px"><svg width="16" height="16"><use href="#ico-person"/></svg>Personnel</div>
    <div class="nav-btn" style="left:422px;top:66px;width:90px;height:32px;font-size:13px;padding-left:6px;gap:5px"><svg width="20" height="20"><use href="#ico-board"/></svg>Training</div>
    <div class="nav-btn" style="left:22px;top:105px;width:83px;height:33px;font-size:13px;padding-left:5px;gap:6px"><svg width="18" height="18"><use href="#ico-cloud"/></svg>Updates</div>
    <div class="nav-btn" style="left:115px;top:105px;width:79px;height:33px;font-size:13px;padding-left:7px;gap:7px"><svg width="16" height="16"><use href="#ico-check"/></svg>Quality</div>
    <div class="nav-btn" style="left:205px;top:105px;width:60px;height:33px;font-size:13px;padding-left:7px;gap:6px"><svg width="17" height="17"><use href="#ico-helmet"/></svg>EHS</div>

    <span class="title" style="left:22px;top:154px;font-size:33px">Scorecard</span>
    <span class="subtitle" style="left:23px;top:186px;font-size:11px">KPI Score by Site</span>
    <span class="period" style="left:23px;top:196px;font-size:12px">Showing July 2013</span>

    <span class="score-label" style="left:332px;top:161px;font-size:21px">Site Score<br>Goal <span class="goal-value">90%</span></span>
    <svg class="gauge" style="left:443px;top:149px" width="66" height="66"><use href="#gauge-ring"/></svg>
    <span class="gauge-value" style="left:443px;top:172px;width:66px;font-size:20px">86%</span>

    <svg class="abs" style="left:0;top:0" width="544" height="482" role="img" aria-label="Bar chart of KPI score by site, July 2013">
      <g font-family="Roboto, Arial, sans-serif" font-size="8.5" fill="#555" text-anchor="end" font-weight="300">
        <text x="67" y="248">100%</text><text x="67" y="275">90%</text><text x="67" y="301">80%</text>
        <text x="67" y="328">70%</text><text x="67" y="355">60%</text><text x="67" y="381">50%</text>
      </g>
      <g stroke="#c9c9c9" stroke-dasharray="2 2">
        <line x1="72" y1="245" x2="506" y2="245"/><line x1="72" y1="272" x2="506" y2="272"/><line x1="72" y1="298" x2="506" y2="298"/>
        <line x1="72" y1="325" x2="506" y2="325"/><line x1="72" y1="352" x2="506" y2="352"/>
      </g>
      <line x1="72" y1="378" x2="506" y2="378" stroke="#999"/>
      <g fill="var(--bar)">
        <rect x="75" y="245" width="12" height="133"/><rect x="90.4" y="272" width="12" height="106"/><rect x="105.8" y="277" width="12" height="101"/>
        <rect x="121.2" y="245" width="12" height="133"/><rect x="136.6" y="261" width="12" height="117"/><rect x="152" y="269" width="12" height="109"/>
        <rect x="167.4" y="245" width="12" height="133"/><rect x="182.8" y="272" width="12" height="106"/><rect x="198.2" y="277" width="12" height="101"/>
        <rect x="213.6" y="245" width="12" height="133"/><rect x="229" y="261" width="12" height="117"/><rect x="244.4" y="269" width="12" height="109"/>
        <rect x="259.8" y="245" width="12" height="133"/><rect x="275.2" y="261" width="12" height="117"/><rect x="290.6" y="269" width="12" height="109"/>
        <rect x="306" y="245" width="12" height="133"/><rect x="321.4" y="272" width="12" height="106"/><rect x="336.8" y="277" width="12" height="101"/>
        <rect x="352.2" y="245" width="12" height="133"/><rect x="367.6" y="261" width="12" height="117"/><rect x="383" y="269" width="12" height="109"/>
        <rect x="398.4" y="269" width="12" height="109"/><rect x="413.8" y="245" width="12" height="133"/><rect x="429.2" y="272" width="12" height="106"/>
        <rect x="444.6" y="277" width="12" height="101"/><rect x="460" y="245" width="12" height="133"/><rect x="475.4" y="261" width="12" height="117"/>
        <rect x="490.8" y="269" width="12" height="109"/>
      </g>
      <g font-family="Roboto, Arial, sans-serif" font-size="6.2" fill="#333" text-anchor="end">
        <text transform="translate(84,386) rotate(-45)">Arden - Alder Park</text>
        <text transform="translate(99.4,386) rotate(-45)">Brio - Bayfield</text>
        <text transform="translate(114.8,386) rotate(-45)">Cova - Cresthaven</text>
        <text transform="translate(130.2,386) rotate(-45)">Dell Ridge - Dunmore Bay</text>
        <text transform="translate(145.6,386) rotate(-45)">Elm - Eastbrook</text>
        <text transform="translate(161,386) rotate(-45)">Fenwick - Fairhill</text>
        <text transform="translate(176.4,386) rotate(-45)">Grove - Glenwood Flats</text>
        <text transform="translate(191.8,386) rotate(-45)">Grove - Hollis</text>
        <text transform="translate(207.2,386) rotate(-45)">Halden - Ironvale</text>
        <text transform="translate(222.6,386) rotate(-45)">Halden - Juniper</text>
        <text transform="translate(238,386) rotate(-45)">Hub - Kingsford</text>
        <text transform="translate(253.4,386) rotate(-45)">Iver - Lowmoor</text>
        <text transform="translate(268.8,386) rotate(-45)">Juno - Millbrook</text>
        <text transform="translate(284.2,386) rotate(-45)">Kestrel - Northgate</text>
        <text transform="translate(299.6,386) rotate(-45)">Lark Labs</text>
        <text transform="translate(315,386) rotate(-45)">Marlow - Oakridge</text>
        <text transform="translate(330.4,386) rotate(-45)">Marlow - Pinecrest</text>
        <text transform="translate(345.8,386) rotate(-45)">Marlow - Quarry Hill</text>
        <text transform="translate(361.2,386) rotate(-45)">Marlow - Northgate</text>
        <text transform="translate(376.6,386) rotate(-45)">Marlow - Redfern</text>
        <text transform="translate(392,386) rotate(-45)">Marlow - Stonebridge</text>
        <text transform="translate(407.4,386) rotate(-45)">Marlow - Thornton</text>
        <text transform="translate(422.8,386) rotate(-45)">Norde - Upland</text>
        <text transform="translate(438.2,386) rotate(-45)">Orin - Westhaven</text>
        <text transform="translate(453.6,386) rotate(-45)">Pell - Yarrow</text>
        <text transform="translate(469,386) rotate(-45)">Pell - Zephyr Point</text>
        <text transform="translate(484.4,386) rotate(-45)">Quill - Ashcombe</text>
        <text transform="translate(499.8,386) rotate(-45)">Rook - Northgate</text>
      </g>
    </svg>
  </section>

  <section class="panel" style="left:628px;top:517px;width:544px;height:483px">
    <span class="brand-dot" style="left:22px;top:22px;width:30px;height:30px"></span>
    <span class="brand-name" style="left:64px;top:29px;font-size:18px">company</span>
    <span class="brand-rule" style="left:145px;top:24px;height:24px"></span>
    <span class="scope" style="left:153px;top:27px;font-size:8.5px">All sites<br>All Programs | July 2013</span>
    <span class="product" style="right:20px;top:24px;font-size:23px">KLTVantor</span>

    <div class="nav-btn" style="left:22px;top:66px;width:100px;height:32px;font-size:13px;padding-left:6px;gap:5px"><svg width="17" height="17"><use href="#ico-org"/></svg>Governance</div>
    <div class="nav-btn" style="left:133px;top:66px;width:61px;height:32px;font-size:13px;padding-left:8px;gap:5px"><svg width="13" height="13"><use href="#ico-bars"/></svg>Cost</div>
    <div class="nav-btn" style="left:207px;top:66px;width:100px;height:32px;font-size:13px;padding-left:6px;gap:5px"><svg width="17" height="17"><use href="#ico-org"/></svg>Innovations</div>
    <div class="nav-btn" style="left:318px;top:66px;width:94px;height:32px;font-size:13px;padding-left:8px;gap:7px"><svg width="16" height="16"><use href="#ico-person"/></svg>Personnel</div>
    <div class="nav-btn" style="left:422px;top:66px;width:90px;height:32px;font-size:13px;padding-left:6px;gap:5px"><svg width="20" height="20"><use href="#ico-board"/></svg>Training</div>
    <div class="nav-btn" style="left:22px;top:105px;width:83px;height:33px;font-size:13px;padding-left:5px;gap:6px"><svg width="18" height="18"><use href="#ico-cloud"/></svg>Updates</div>
    <div class="nav-btn" style="left:115px;top:105px;width:79px;height:33px;font-size:13px;padding-left:7px;gap:7px"><svg width="16" height="16"><use href="#ico-check"/></svg>Quality</div>
    <div class="nav-btn" style="left:205px;top:105px;width:60px;height:33px;font-size:13px;padding-left:7px;gap:6px"><svg width="17" height="17"><use href="#ico-helmet"/></svg>EHS</div>

    <span class="title" style="left:22px;top:154px;font-size:33px">Scorecard</span>
    <span class="subtitle" style="left:23px;top:186px;font-size:11px">KPI Score by Site</span>
    <span class="period" style="left:23px;top:196px;font-size:12px">Showing July 2013</span>

    <span class="score-label" style="left:332px;top:161px;font-size:21px">Site Score<br>Goal <span class="goal-value">90%</span></span>
    <svg class="gauge" style="left:443px;top:149px" width="66" height="66"><use href="#gauge-ring"/></svg>
    <span class="gauge-value" style="left:443px;top:172px;width:66px;font-size:20px">86%</span>
  </section>

  <table class="kpi-table small-table">
    <tr><th style="width:140px">Key Performance Indicator</th><th class="num" style="width:40px">KPI<br>Score</th><th style="width:225px">Target</th><th class="num" style="width:50px">Score<br>Points</th><th class="num" style="width:52px">Possible<br>Points</th></tr>
    <tr><td>Complaints</td><td class="num miss">4.0</td><td>Less than control limit of 4 complaints per month</td><td class="num miss">3</td><td class="num">5</td></tr>
    <tr><td>Quality Audits</td><td class="num">3.2</td><td>3 out of 5 average on all internal and joint audits</td><td class="num">10</td><td class="num">10</td></tr>
    <tr><td>Customer Surveys</td><td class="num">4.7</td><td>4 out of 5 average monthly survey score</td><td class="num">5</td><td class="num">5</td></tr>
    <tr><td>Work Order Completion</td><td class="num">100%</td><td>100% percent on-time monthly completion</td><td class="num">5</td><td class="num">5</td></tr>
    <tr><td>Employees Trained</td><td class="num">100%</td><td>90% or greater</td><td class="num">5</td><td class="num">5</td></tr>
    <tr><td>Recordable Rate</td><td class="num">1.1</td><td>Less than 1.9</td><td class="num">10</td><td class="num">10</td></tr>
    <tr><td>Near Misses</td><td class="num">8.0</td><td>Less than control limit of 10 near misses per month</td><td class="num">5</td><td class="num">5</td></tr>
    <tr class="total"><td>TOTAL</td><td></td><td></td><td class="num">42</td><td class="num">45</td></tr>
  </table>
</div>
</body>
</html>
```